Marlowe Tots Wipes Packaging

Brand: Marlowe Tots
Packaging needed: Baby Wipes

Create a new brand for baby wipes called Marlowe Tots. This logo can include character/icons geared towards the baby/parent market.

Use Tavvies/Dorlins for copy reference for now.

**Please note that we would like to see more festive cartoon options like the characters such as Tilly Thimbledown. More colorful colors and characters.*****

Target Market(s)

Parents/Mothers

Industry/Entity Type

Baby

```html
<!DOCTYPE html>
<html lang="en">
<head>
<meta charset="utf-8">
<title>Marlowe Tots Baby Wipes</title>
<link rel="stylesheet" href="https://fonts.googleapis.com/css2?family=Marcellus&family=Lato:wght@400;700;900&family=Arimo:wght@400&display=swap">
<style>
  :root {
    --page: #ffffff;
    --sky: #c3e7f2;
    --sky-deep: #a8d3e3;
    --navy: #0d3b94;
    --royal: #3366e6;
    --white: #ffffff;
    --badge-text: #a9d3e3;
  }
  * { margin: 0; padding: 0; box-sizing: border-box; }
  html, body {
    width: 1200px;
    height: 900px;
    overflow: hidden;
    background: var(--page);
  }
  .canvas {
    position: relative;
    width: 1200px;
    height: 900px;
    background: var(--page);
  }
  .label-art {
    position: absolute;
    left: 0;
    top: 0;
    width: 1200px;
    height: 900px;
  }
  .brand-name {
    position: absolute;
    left: 74px;
    top: 180px;
    font-family: "Marcellus", serif;
    font-size: 100px;
    font-weight: 400;
    line-height: 1;
    color: var(--navy);
    white-space: nowrap;
  }
  .product-name {
    position: absolute;
    left: 184px;
    top: 326px;
    font-family: "Marcellus", serif;
    font-size: 62px;
    font-weight: 400;
    line-height: 1;
    color: var(--navy);
    white-space: nowrap;
  }
  .features {
    position: absolute;
    left: 191px;
    top: 400px;
    list-style: none;
    font-family: "Arimo", Arial, sans-serif;
    font-size: 22px;
    line-height: 27px;
    color: var(--royal);
    white-space: nowrap;
  }
  .count-badge {
    position: absolute;
    left: 76px;
    top: 562px;
    width: 100px;
    font-family: "Lato", Arial, sans-serif;
    font-weight: 900;
    font-style: italic;
    font-size: 52px;
    line-height: 1;
    text-align: center;
    color: var(--badge-text);
  }
  .pack-info {
    position: absolute;
    left: 116px;
    top: 702px;
    font-family: "Arimo", Arial, sans-serif;
    font-size: 20px;
    line-height: 26px;
    color: var(--white);
    white-space: nowrap;
  }
</style>
</head>
<body>
<main class="canvas">
  <svg class="label-art" viewBox="0 0 1200 900" xmlns="http://www.w3.org/2000/svg">
    <defs>
      <clipPath id="label-shape">
        <rect x="26" y="115" width="1146" height="653" rx="72" ry="72"/>
      </clipPath>
      <radialGradient id="photo-tones" cx="880" cy="540" r="360" gradientUnits="userSpaceOnUse">
        <stop offset="0" stop-color="#f0c9b4"/>
        <stop offset="0.35" stop-color="#e9cfc6"/>
        <stop offset="0.55" stop-color="#9fb3dd"/>
        <stop offset="0.75" stop-color="#d9ecf4"/>
        <stop offset="1" stop-color="#eef7fb"/>
      </radialGradient>
    </defs>
    <g clip-path="url(#label-shape)">
      <rect class="label-bg" x="26" y="115" width="1146" height="653" fill="var(--sky)"/>
      <path class="wave-white" d="M26,430 C110,590 240,640 420,610 C640,570 820,330 1172,175 L1172,768 L26,768 Z" fill="var(--white)"/>
      <path class="wave-deep" d="M26,470 C110,615 240,660 420,635 C640,600 820,400 1172,300 L1172,768 L26,768 Z" fill="var(--sky-deep)"/>
      <path class="photo-area" role="img" aria-label="Photo of a smiling baby in a blue sun hat lying on a soft white blanket"
            d="M500,768 L500,590 C660,540 840,330 1172,200 L1172,768 Z" fill="url(#photo-tones)"/>
    </g>
    <g class="count-card">
      <path d="M62,548 L176,536 L187,636 L90,656 L72,652 Z" fill="var(--white)"/>
      <path d="M176,616 L187,636 L170,640 Z" fill="#e6f3f8"/>
    </g>
  </svg>

  <h1 class="brand-name">Marlowe Tots</h1>
  <h2 class="product-name">Baby Wipes</h2>
  <ul class="features">
    <li>Unscented | Hypoallergenic</li>
    <li>Natural Aloe | Soap Free</li>
    <li>Alcohol Free</li>
    <li>Dermatologically Tested</li>
  </ul>
  <div class="count-badge">70</div>
  <p class="pack-info">70 WIPES LINGETTES TOALLITAS<br>17.8cm x 17.8cm (7.0 in/po x 7.0 in/po)</p>
</main>
</body>
</html>
```